Web Design Project for NCYB

Hi,
I am looking for a website design for the Northern Council for Youth Boards.
This is an organisation which helps with legal disputes and other challenges which involve children.  The company want a web page which is professional but friendly.  The purpose of the website is to explain what the organisation does and to give people a place where they can download documents and information.
The homepage will have a video on the page.  ALSO, we would prefer the site to have a left hand navigation (not a top navigation).
I have enclosed the logo, a picture of the old (rubbish) home page and a screenshot from the video (you are welcome to change the dimensions).
If you have any questions, please ask.
-K
UPDATE: 6th DECEMBER:
Thanks for the designs so far.  I promise to give feedback to every single person.  In the meantime, can I just say that there's some good designs so far but I don't think anyone has nailed this yet.
So, I am uploading a screenshot called "theylikethis.jpg".  This is a screenshot from a website that the client says they like.
Can I also say, it's okay to reduce the size of the video.  I'm seeing a lot of massive videos.
Thanks folks!
UPDATE:  You can view a live demo of the site that they like at www.demohostqz.co.uk
UPDATE:  I've just found another good example of a site with a left nav at www.brightresourcehubnet.com

Hi,
Hi folks,
Had a quick look at the designs and just to say how impressed I am with the qualityand choice. There are a few that caught my eye and I'll try and narrow them down.I've also passed the link onto the other representatives for their input beforemaking a final choice. If I don't hear from any of the other represenatatives by Wednesday, I'll chose adesign and let you know. Once again many thanks for the quick response in gettingdesigns done and really looking forward to seeing the completed website.
Industry/Entity Type
Legal
Requirements
Must have
- a video player (any size of your choosing)
a left side navigation
the logo

```html
<!DOCTYPE html>
<html lang="en">
<head>
<meta charset="utf-8">
<title>Northern Council for Youth Boards</title>
<link href="https://fonts.googleapis.com/css2?family=PT+Sans:wght@400;700&family=Arimo:wght@400;700&family=Cinzel:wght@400;700&display=swap" rel="stylesheet">
<style>
:root{
  --sky:#d4eff6;
  --pale:#cdeef6;
  --panel:#d9f3f8;
  --navy:#0f3a8f;
  --royal:#1d4aa8;
  --text:#222;
  --grey:#9a9a9a;
  --line:#c9c9c9;
  --cream:#ecebe2;
  --green:#5fc13a;
}
*{box-sizing:border-box;margin:0;padding:0}
html,body{width:1020px;height:1200px;overflow:hidden}
body{background:var(--sky);font-family:"Arimo",Arial,sans-serif;color:var(--text);position:relative}
.abs{position:absolute}
.page{left:101px;top:17px;width:818px;height:1183px;background:#fff;border-radius:14px 14px 0 0;border:1px solid #e4e4e4}
.header-band{left:102px;top:43px;width:816px;height:43px;background:var(--pale);border-top:1px solid #bfe6ef;border-bottom:1px solid #bfe6ef}
.brand{left:154px;top:24px;width:77px;height:61px;background:#fff;display:flex;align-items:center;gap:5px;padding-left:4px}
.brand-mark{width:14px;height:14px;background:var(--navy)}
.brand-name{font-family:"PT Sans",sans-serif;font-weight:700;font-size:17px;color:var(--navy)}
.org-title{left:275px;top:50px;font-family:"Cinzel",serif;font-weight:700;font-size:20px;color:var(--navy);letter-spacing:.3px}

.video{width:245px;height:194px;background:var(--sky);border:4px dotted #8fdcef;border-radius:6px;padding:9px}
.video-inner{width:100%;height:100%;background:#fff;border:3px double #cfcfcf;padding:7px}
.video-still{width:100%;height:100%;background:linear-gradient(180deg,#eef2ee 0%,#dfe4df 60%,#3a3230 100%);position:relative}
.play{position:absolute;left:50%;top:42%;transform:translate(-50%,-50%)}

.heading{font-family:"PT Sans",sans-serif;font-size:22px;color:var(--navy)}
.nav{left:111px;top:364px;width:166px;height:258px;border:1px solid var(--line);padding:4px}
.nav-inner{border:1px solid var(--line);height:100%;padding-top:12px}
.nav a{display:block;height:25.4px;line-height:25.4px;padding-left:10px;font-family:"PT Sans",sans-serif;font-size:14px;color:var(--navy);text-decoration:none}
.nav a.active{background:var(--navy);color:#fff}
.photo{display:block}

.subhead{left:316px;top:555px;font-family:"Arimo",sans-serif;font-weight:700;font-size:16px;color:var(--navy)}
.copy{left:316px;width:390px;font-size:11.5px;line-height:18.6px;color:#333}
.read-more{display:flex;align-items:center;gap:6px;font-size:12.5px;color:var(--navy)}

.feature{left:315px;width:391px;background:var(--panel);border-top:3px solid var(--navy);border-bottom:3px solid var(--navy);border-left:1px solid #9fcfe0;border-right:1px solid #9fcfe0}
.feature-tab{position:absolute;right:0;top:0;width:184px;height:24px;background:var(--navy);color:#fff;font-size:15px;line-height:24px;padding-left:9px}
.feature-thumb{position:absolute;left:9px;top:28px;width:119px;height:96px}
.feature-body{position:absolute;left:139px;top:32px;width:245px}
.feature-body h3{font-weight:400;font-size:15.5px;color:#111;margin-bottom:3px}
.feature-body p{font-size:11.5px;line-height:17.6px;color:#222}
.feature .read-more{position:absolute;right:14px;color:#111;font-size:12px}

.footer{left:315px;top:1140px;width:390px;height:42px;background:var(--panel);border-top:1px dotted #a9d8e6;border-bottom:1px dotted #a9d8e6;text-align:center;line-height:42px;font-size:10.5px;color:var(--navy)}

.search-btn{left:891px;top:364px;width:18px;height:18px;background:#eee;border:1px solid #999;border-radius:2px}
.search-box{left:738px;top:388px;width:172px;height:157px;border:1px solid #bbb;padding:4px;box-shadow:0 2px 3px #ddd}
.search-inner{border:1px solid #ccc;height:100%;padding:29px 13px}
.subscribe{background:linear-gradient(135deg,#cdeef6,#e6f7fb);padding:11px 5px 6px;text-align:center}
.subscribe label{display:block;font-size:12px;color:var(--navy);margin-bottom:5px;text-align:left}
.subscribe .field{height:18px;background:#fff;border:1px solid #aaa;margin-bottom:10px}
.subscribe .btn{display:inline-block;padding:1px 10px;border:1px solid #888;border-radius:3px;background:#f1f1f1;font-size:11.5px;color:#111}

.social{display:flex;align-items:center;gap:5px;font-family:"Arimo",sans-serif;font-weight:700;font-size:14px;color:var(--royal)}
.dot{width:12px;height:12px;border-radius:50%;background:var(--royal)}
.sq{width:12px;height:12px;background:var(--royal)}

.list-box{left:740px;width:169px;background:var(--cream);border:2px solid var(--royal);border-radius:3px;padding:8px 0 0 4px}
.list-box li{list-style:none;display:flex;align-items:center;gap:9px;height:29.7px;font-size:12px;color:#222;letter-spacing:-.2px}
</style>
</head>
<body>
<div class="abs page"></div>
<div class="abs header-band"></div>
<div class="abs brand"><span class="brand-mark"></span><span class="brand-name">NCYB</span></div>
<div class="abs org-title">Northern Council for Youth Boards</div>

<div class="abs video" style="left:111px;top:117px">
  <div class="video-inner"><div class="video-still" role="img" aria-label="Video still of a presenter speaking to camera">
    <svg class="play" width="42" height="42" viewBox="0 0 42 42"><path d="M6 3 L38 21 L6 39 Z" fill="#1d3fb0" opacity=".85"/></svg></div></div>
</div>
<div class="abs video" style="left:389px;top:117px">
  <div class="video-inner"><div class="video-still" role="img" aria-label="Video still of a presenter speaking to camera">
    <svg class="play" width="42" height="42" viewBox="0 0 42 42"><path d="M6 3 L38 21 L6 39 Z" fill="#1d3fb0" opacity=".85"/></svg></div></div>
</div>
<div class="abs video" style="left:665px;top:117px">
  <div class="video-inner"><div class="video-still" role="img" aria-label="Video still of a presenter speaking to camera">
    <svg class="play" width="42" height="42" viewBox="0 0 42 42"><path d="M6 3 L38 21 L6 39 Z" fill="#1d3fb0" opacity=".85"/></svg></div></div>
</div>

<h2 class="abs heading" style="left:114px;top:333px">Categories</h2>
<nav class="abs nav"><div class="nav-inner">
  <a href="#">Home</a><a href="#" class="active">About Us</a><a href="#">News</a><a href="#">Confrences</a><a href="#">Minutes</a><a href="#">Annual Reports</a><a href="#">Archive</a><a href="#">Contact Us</a><a href="#">Links</a>
</div></nav>
<div class="abs photo" style="left:127px;top:633px;width:143px;height:221px;background:linear-gradient(180deg,#c9d3e6 0%,#7f8fb4 50%,#2a2f45 100%)" role="img" aria-label="Globe above a group of business silhouettes"></div>
<div class="abs photo" style="left:123px;top:867px;width:150px;height:270px;background:linear-gradient(160deg,#e6ecf6 0%,#8a9cc4 50%,#3b4a78 100%)" role="img" aria-label="Blurred business people walking through a bright hall"></div>

<h2 class="abs heading" style="left:316px;top:334px">A Few Words About Us</h2>
<div class="abs photo" style="left:313px;top:366px;width:391px;height:175px;background:linear-gradient(180deg,#9fb8d8 0%,#dfe8f1 55%,#c8cdd4 100%)" role="img" aria-label="Two business people in front of a cloudy sky">
  <span class="abs" style="right:12px;bottom:20px;font-family:'PT Sans',sans-serif;font-weight:700;font-size:18px;color:#222">Company Profile</span>
</div>
<h3 class="abs subhead">Aliquam eu posuere risus</h3>
<p class="abs copy" style="top:604px">Aenean dignissim accumsan nibh, nec pulvinar neque ultricies eget. Mauris tempus risus sed nulla aliquam molestie. Nunc lobortis, arcu ut lacinia tincid-unt, mi ante ullamcorper metus, in fringilla neque felis eget dolor.</p>
<p class="abs copy" style="top:679px">Proin lacinia libero semper nisl mollis et ultrices neque hendrerit. Pellen-tesque interdum</p>
<div class="abs read-more" style="left:622px;top:735px">
  <svg width="20" height="20" viewBox="0 0 20 20"><path d="M7 0h6v7h7v6h-7v7H7v-7H0V7h7z" fill="var(--green)"/></svg>Read More</div>

<section class="abs feature" style="top:773px;height:152px">
  <div class="feature-tab">Another Title Here</div>
  <div class="feature-thumb" role="img" aria-label="Small figures standing on puzzle pieces" style="background:linear-gradient(180deg,#fafafa,#d9dde2)"></div>
  <div class="feature-body"><h3>Dolorest Ipsum Elit Aliwua</h3>
    <p>Lorem ipsum dolor sit amet, consectetur adipisicing elit, sed do eiusmod tempor incididunt ut labore et dolore magna aliqua. Ut enim ad minim veniam, quis nostrud.</p></div>
  <div class="read-more" style="top:127px"><svg width="14" height="14" viewBox="0 0 14 14"><circle cx="7" cy="7" r="6" fill="#fff" stroke="#eed"/><path d="M5 4l4 3-4 3z" fill="#e070d0"/></svg>&nbsp;Read More</div>
</section>

<section class="abs feature" style="top:962px;height:152px">
  <div class="feature-tab">Some Title Here</div>
  <div class="feature-thumb" role="img" aria-label="Businessman standing against a cloudy sky" style="width:114px;height:94px;background:linear-gradient(90deg,#3a4050,#b9c6d4 60%,#eef2f6)"></div>
  <div class="feature-body"><h3>Lorest Ut Labore Sed</h3>
    <p>Lorem ipsum dolor sit amet, consectetur adipisicing elit, sed do eiusmod tempor incididunt ut labore et dolore magna aliqua.</p></div>
  <div class="read-more" style="top:128px"><svg width="14" height="14" viewBox="0 0 14 14"><circle cx="7" cy="7" r="6" fill="#fff" stroke="#eed"/><path d="M5 4l4 3-4 3z" fill="#e070d0"/></svg>&nbsp;Read More</div>
</section>

<footer class="abs footer">Copyright 2012 Website name</footer>

<h2 class="abs heading" style="left:742px;top:332px">Search</h2>
<div class="abs search-btn"><svg width="16" height="16" viewBox="0 0 16 16"><path d="M3 7h6V4l4 4-4 4V9H3z" fill="#222"/></svg></div>
<div class="abs search-box"><div class="search-inner"><div class="subscribe">
  <label>Enter Your Email Address:</label><div class="field"></div><span class="btn">Subscribe</span>
</div></div></div>

<div class="abs social" style="left:742px;top:610px"><span class="dot"></span>Chirpline</div>
<div class="abs social" style="left:832px;top:610px"><span class="sq"></span>Pagebook</div>

<h2 class="abs heading" style="left:742px;top:676px">Loreum Ipsum</h2>
<ul class="abs list-box" style="top:710px;height:165px">
  <li><svg width="20" height="20" viewBox="0 0 20 20"><path d="M10 1l2.6 6.2 6.6.5-5 4.3 1.6 6.5L10 15l-5.8 3.5 1.6-6.5-5-4.3 6.6-.5z" fill="#9fb0d8" stroke="var(--royal)"/></svg>Lorest Mest Alpus Trips</li>
  <li><svg width="20" height="20" viewBox="0 0 20 20"><path d="M10 1l2.6 6.2 6.6.5-5 4.3 1.6 6.5L10 15l-5.8 3.5 1.6-6.5-5-4.3 6.6-.5z" fill="#9fb0d8" stroke="var(--royal)"/></svg>Forum Magnus</li>
  <li><svg width="20" height="20" viewBox="0 0 20 20"><path d="M10 1l2.6 6.2 6.6.5-5 4.3 1.6 6.5L10 15l-5.8 3.5 1.6-6.5-5-4.3 6.6-.5z" fill="#9fb0d8" stroke="var(--royal)"/></svg>Tucit Alowet Dolorest Et</li>
  <li><svg width="20" height="20" viewBox="0 0 20 20"><path d="M10 1l2.6 6.2 6.6.5-5 4.3 1.6 6.5L10 15l-5.8 3.5 1.6-6.5-5-4.3 6.6-.5z" fill="#9fb0d8" stroke="var(--royal)"/></svg>Magnus Quisit</li>
  <li><svg width="20" height="20" viewBox="0 0 20 20"><path d="M10 1l2.6 6.2 6.6.5-5 4.3 1.6 6.5L10 15l-5.8 3.5 1.6-6.5-5-4.3 6.6-.5z" fill="#9fb0d8" stroke="var(--royal)"/></svg>Bern Excitir At Allust</li>
</ul>

<h2 class="abs heading" style="left:743px;top:900px">Loreum Ipsum</h2>
<ul class="abs list-box" style="top:940px;height:165px">
  <li><svg width="20" height="20" viewBox="0 0 20 20"><path d="M10 1l2.6 6.2 6.6.5-5 4.3 1.6 6.5L10 15l-5.8 3.5 1.6-6.5-5-4.3 6.6-.5z" fill="#9fb0d8" stroke="var(--royal)"/></svg>Grilled Steak Forte</li>
  <li><svg width="20" height="20" viewBox="0 0 20 20"><path d="M10 1l2.6 6.2 6.6.5-5 4.3 1.6 6.5L10 15l-5.8 3.5 1.6-6.5-5-4.3 6.6-.5z" fill="#9fb0d8" stroke="var(--royal)"/></svg>Maple Butternut Squash</li>
  <li><svg width="20" height="20" viewBox="0 0 20 20"><path d="M10 1l2.6 6.2 6.6.5-5 4.3 1.6 6.5L10 15l-5.8 3.5 1.6-6.5-5-4.3 6.6-.5z" fill="#9fb0d8" stroke="var(--royal)"/></svg>Tri-Onion Wild Rice</li>
  <li><svg width="20" height="20" viewBox="0 0 20 20"><path d="M10 1l2.6 6.2 6.6.5-5 4.3 1.6 6.5L10 15l-5.8 3.5 1.6-6.5-5-4.3 6.6-.5z" fill="#9fb0d8" stroke="var(--royal)"/></svg>Perfect Together: Chicken</li>
  <li><svg width="20" height="20" viewBox="0 0 20 20"><path d="M10 1l2.6 6.2 6.6.5-5 4.3 1.6 6.5L10 15l-5.8 3.5 1.6-6.5-5-4.3 6.6-.5z" fill="#9fb0d8" stroke="var(--royal)"/></svg>Mexican Taco Salad</li>
</ul>
</body>
</html>
```